Reboot of current Powerpoint Design

We would like to modernise our current powerpoint design which we use for the delivery of class room based training to 5-10 trainees at a time. We have attached our current design but would like a more updated (yet still practical for in-house edits and development).
We would like to be left with a collection of no more than 10-20 master slides for ongoing use in the business. Critically the slides should be focussed on being able to be easily read in a classroom environment, have minimal or no animation (easy to operate by a trainer) and should recognise our customer base which is largely fairly conservative (heavy industry).
In short we are seeking a professional and engaging end result which mirrors our current branding.
Across our entire range of courses we will use the following key structure:
- Title
- Introductory slides
- Overviews
- Modules
- Content
- Discussion
- Conclusion
As part of this update we would like to increase our use of photos (noting that we are not limited to the photos in the current powerpoint so any design should simply use placeholders).
The updated version should incorporate our current branding which is represented in the attached example powerpoint as well as our website (www.ironleafalliance-demo.com).
Thanks
Glen
Target Market(s)
Safety and compliance in heavy industries (eg. mining, manufacturing, construction, etc.)
Industry/Entity Type
Training
Font styles to use
Other font styles liked:
- Helvetica (or similar to be used on windows machines)
Colors
Requirements
Must have
- Approximately 20 master slides that can be easily applied across a large number of current power point presentations.
- Strong visual focus with main use in classroom environment (so note that these are used on a projector screen - please take into account (eg. no small fonts).
- We generally use the notes section for any detailed information (trainer benefit) so our focus is on using the slides as triggers for conversations, training structure and headline topics.
- If anything we are focussed on a less is more mentality and are looking for a clean, simple and professional appeal. Note we have no issue in some of the content of the example slides (CPR) moving to the notes section.
- We have also just begun implementing a new brand bi-line which is:
- ThinkSafe. ActSafe. Ironleaf. (Note the Safe. in each word is in BOLD).
- This bi-line needs to be incorporated along with the Ironleaf Alliance logo in each slide. Please note that we also use the unique A design in the Ironleaf Alliance logo as a further design feature in our branding documents. As per current powerpoint, we would prefer this to be incorporated as well.
Nice to have
- Functional graphics (easy to edit) and branded icons to ensure we continue to push the Ironleaf Alliance brand throughout the presentations.
Should not have
- Animation and difficult to edit slides.

```html
<!DOCTYPE html>
<html lang="en">
<head>
<meta charset="utf-8">
<title>Respond to an Emergency Situation</title>
<link href="https://fonts.googleapis.com/css2?family=Questrial&family=Montserrat:wght@400;700;800&display=swap" rel="stylesheet">
<style>
  :root {
    --navy: #2b3d54;
    --navy-deep: #1f3046;
    --navy-mist: #4a6079;
    --footer: #22334a;
    --red: #c8203a;
    --grey: #b7b9bb;
    --grey-dark: #9ea1a4;
    --icon-ink: #3d4652;
    --white: #ffffff;
    --soft-white: #d9dbdd;
    --badge-grey: #8d8f92;
  }
  * { box-sizing: border-box; margin: 0; padding: 0; }
  html, body { width: 1200px; height: 640px; overflow: hidden; background: var(--navy); }
  .slide {
    position: relative; width: 1200px; height: 640px; overflow: hidden;
    font-family: "Questrial", "Century Gothic", sans-serif; color: var(--white);
  }
  .slide-photo {
    position: absolute; inset: 0;
    background:
      radial-gradient(ellipse 380px 160px at 560px 380px, rgba(190,200,212,0.30), transparent 70%),
      linear-gradient(180deg, var(--navy-mist) 0%, var(--navy) 45%, var(--navy-deep) 100%);
  }
  .slide-title {
    position: absolute; left: 49px; top: 28px;
    font-size: 49px; font-weight: 400; letter-spacing: 1.2px; text-transform: uppercase;
    white-space: nowrap;
  }
  .process { position: absolute; inset: 0; }
  .step-text {
    position: absolute; width: 220px; margin-left: -110px;
    text-align: center; font-size: 18px; line-height: 22.5px;
  }
  .step-badge {
    position: absolute; width: 32px; height: 32px; margin: -16px 0 0 -16px; border-radius: 50%;
    font-family: "Montserrat", sans-serif; font-weight: 800; font-size: 14px;
    display: flex; align-items: center; justify-content: center; color: var(--white);
  }
  .step-badge.grey { background: var(--badge-grey); }
  .step-badge.red { background: var(--red); }
  .footer {
    position: absolute; left: 0; right: 0; bottom: 0; height: 46px; background: var(--footer);
    display: flex; align-items: center; padding: 0 40px 0 60px;
  }
  .brand {
    display: flex; align-items: center; gap: 8px;
    font-family: "Montserrat", sans-serif; font-weight: 800; font-size: 15px;
    text-transform: uppercase; letter-spacing: 0.3px; color: var(--white);
  }
  .brand-mark { width: 10px; height: 10px; background: var(--red); }
  .byline {
    margin-left: 48px; font-family: "Montserrat", sans-serif; font-weight: 400;
    font-size: 14px; color: var(--white); letter-spacing: 0.2px;
  }
  .byline b { font-weight: 800; }
  .site-url { margin-left: auto; font-size: 14px; }
  .page-num { margin-left: 60px; font-size: 12px; }
</style>
</head>
<body>
<main class="slide">
  <div class="slide-photo" role="img" aria-label="Blurred night photo of an ambulance speeding along a road"></div>

  <h1 class="slide-title">1. Respond to an emergency situation</h1>

  <svg class="process" viewBox="0 0 1200 640" width="1200" height="640" aria-hidden="true">
    <polygon points="196,311 398,311 418,331 398,351 196,351 216,331" fill="var(--grey)"/>
    <polygon points="398,311 598,311 618,331 598,351 398,351 418,331" fill="var(--red)"/>
    <polygon points="600,311 798,311 818,331 798,351 600,351 620,331" fill="var(--grey)"/>
    <polygon points="800,311 1002,311 1022,331 1002,351 800,351 820,331" fill="var(--red)"/>

    <g stroke="var(--grey)" stroke-width="1.2">
      <line x1="300" y1="270" x2="300" y2="331"/>
      <line x1="500" y1="331" x2="500" y2="397"/>
      <line x1="700" y1="270" x2="700" y2="331"/>
      <line x1="899" y1="331" x2="899" y2="397"/>
    </g>
    <g fill="var(--soft-white)">
      <circle cx="300" cy="331" r="3.5"/><circle cx="500" cy="331" r="3.5"/>
      <circle cx="700" cy="331" r="3.5"/><circle cx="899" cy="331" r="3.5"/>
    </g>

    <g class="icon-search">
      <circle cx="300" cy="235" r="35" fill="var(--grey-dark)"/>
      <circle cx="296" cy="231" r="11" fill="none" stroke="var(--icon-ink)" stroke-width="2.5"/>
      <polyline points="291,231 295,235 301,227" fill="none" stroke="var(--icon-ink)" stroke-width="2.2"/>
      <line x1="304" y1="239" x2="313" y2="248" stroke="var(--icon-ink)" stroke-width="3.5" stroke-linecap="round"/>
    </g>
    <g class="icon-idea">
      <circle cx="500" cy="432" r="35" fill="var(--red)"/>
      <circle cx="500" cy="426" r="9" fill="none" stroke="var(--white)" stroke-width="2.2"/>
      <rect x="495" y="435" width="10" height="7" rx="1.5" fill="var(--white)"/>
      <g stroke="var(--white)" stroke-width="2" stroke-linecap="round">
        <line x1="500" y1="410" x2="500" y2="413"/><line x1="486" y1="418" x2="489" y2="420"/>
        <line x1="514" y1="418" x2="511" y2="420"/>
      </g>
    </g>
    <g class="icon-target">
      <circle cx="700" cy="235" r="35" fill="var(--grey-dark)"/>
      <circle cx="700" cy="235" r="13" fill="none" stroke="var(--icon-ink)" stroke-width="2.2"/>
      <g stroke="var(--icon-ink)" stroke-width="2.2">
        <line x1="700" y1="216" x2="700" y2="224"/><line x1="700" y1="246" x2="700" y2="254"/>
        <line x1="681" y1="235" x2="689" y2="235"/><line x1="711" y1="235" x2="719" y2="235"/>
      </g>
      <circle cx="700" cy="235" r="4" fill="var(--icon-ink)"/>
    </g>
    <g class="icon-medical">
      <circle cx="899" cy="432" r="35" fill="var(--red)"/>
      <rect x="894" y="417" width="10" height="30" rx="1.5" fill="var(--white)"/>
      <rect x="884" y="427" width="30" height="10" rx="1.5" fill="var(--white)"/>
    </g>
  </svg>

  <span class="step-badge grey" style="left:300px;top:381px">01</span>
  <span class="step-badge red" style="left:500px;top:292px">02</span>
  <span class="step-badge grey" style="left:700px;top:381px">03</span>
  <span class="step-badge red" style="left:899px;top:292px">04</span>

  <p class="step-text" style="left:300px;top:408px">Recognise an<br>emergency<br>situation</p>
  <p class="step-text" style="left:500px;top:147px">Identify, assess and<br>minimise immediate<br>hazards to health<br>and safety of self<br>and others.</p>
  <p class="step-text" style="left:700px;top:408px">Assess the casualty<br>and recognise the<br>need for CPR.</p>
  <p class="step-text" style="left:899px;top:192px">Seek assistance<br>from emergency<br>response services.</p>

  <footer class="footer">
    <span class="brand"><span class="brand-mark"></span>Ironleaf Alliance</span>
    <span class="byline">Think<b>Safe.</b> Act<b>Safe.</b> Ironleaf.</span>
    <span class="site-url">www.ironleafalliance-demo.com</span>
    <span class="page-num">6</span>
  </footer>
</main>
</body>
</html>
```